Portal Panel Medic need professional looking business card printed on plastic, Commericial, Industri

We are family owned and operated garage door company in Indianapolis, Indiana. We sale service and install dock equipment, doors, operators. We are looking to expand our commercial/ industrial division. We also service all residential doors and operators. We are looking for a business that stands out of the crowd. We are committed to have the best customer service in the industry.

Target Market(s)

National and local general contractors, National/ Corpate service accounts,

Industry/Entity Type

Business Service

Contact Information for Business Card

To be printed on plastic stock

Font styles to use
Sans Serif

Colors
ffffff
f04a50
ec1f27

Requirements
Must have
• Name, website,email, phone number, position.
Nice to have
• A standout professional design

```html
<!DOCTYPE html>
<html lang="en">
<head>
<meta charset="utf-8">
<title>Portal Panel Medic — Business Cards</title>
<link href="https://fonts.googleapis.com/css2?family=Arimo:wght@400&family=Lato:wght@700&display=swap" rel="stylesheet">
<style>
  :root {
    --card-white: #ffffff;
    --brand-red: #ec1f27;
    --accent-red: #f04a50;
    --ink: #1f1f1f;
    --divider: #e6e6e6;
    --backdrop: #ecebea;
  }
  * { margin: 0; padding: 0; box-sizing: border-box; }
  html, body { width: 1200px; height: 900px; overflow: hidden; }
  body {
    background: var(--backdrop);
    display: flex;
    align-items: center;
    justify-content: center;
    gap: 60px;
    font-family: "Arimo", Arial, sans-serif;
  }
  .card {
    width: 525px;
    height: 300px;
    background: var(--card-white);
    box-shadow: 0 2px 10px rgba(0,0,0,0.12);
    position: relative;
  }
  .brand-name {
    display: flex;
    align-items: center;
    gap: 8px;
    font-family: "Lato", Arial, sans-serif;
    font-weight: 700;
    color: var(--brand-red);
    text-transform: uppercase;
    letter-spacing: 0.4px;
    white-space: nowrap;
  }
  .brand-dot {
    width: 10px;
    height: 10px;
    border-radius: 50%;
    background: var(--brand-red);
    flex: none;
  }
  /* Front: identity + contact */
  .card-front { display: flex; }
  .card-front .brand-side {
    width: 255px;
    display: flex;
    align-items: center;
    justify-content: center;
    border-right: 1px solid var(--divider);
  }
  .card-front .brand-name { font-size: 19px; }
  .contact-side { padding: 52px 0 0 24px; }
  .person-name {
    color: var(--brand-red);
    font-size: 19px;
    text-transform: uppercase;
    letter-spacing: 0.3px;
  }
  .person-role { color: var(--ink); font-size: 14px; margin: 2px 0 0 8px; }
  .contact-list { list-style: none; margin: 26px 0 0 8px; }
  .contact-list li {
    display: flex;
    align-items: center;
    gap: 8px;
    font-size: 15px;
    color: var(--ink);
    margin-bottom: 3px;
  }
  .contact-list svg { width: 11px; height: 11px; fill: var(--brand-red); flex: none; }
  /* Back: brand + tagline */
  .card-back {
    display: flex;
    flex-direction: column;
    align-items: center;
    justify-content: center;
  }
  .card-back .brand-name { font-size: 28px; margin-top: -10px; }
  .tagline {
    margin-top: 56px;
    font-family: "Lato", Arial, sans-serif;
    font-weight: 700;
    font-size: 14px;
    color: var(--brand-red);
    text-transform: uppercase;
    letter-spacing: 0.4px;
  }
</style>
</head>
<body>
  <section class="card card-front">
    <div class="brand-side">
      <p class="brand-name"><span class="brand-dot"></span>Portal Panel Medic</p>
    </div>
    <div class="contact-side">
      <p class="person-name">Marcus Bellamy</p>
      <p class="person-role">Managing Director</p>
      <ul class="contact-list">
        <li>
          <svg viewBox="0 0 12 12" aria-hidden="true"><path d="M1 4c0-2 2-3 3-3l1 2-1 1c.6 1.4 1.6 2.4 3 3l1-1 2 1c0 1-1 3-3 3C3.5 10 1 7.5 1 4z"/></svg>
          <span>444 555 7291</span>
        </li>
        <li>
          <svg viewBox="0 0 12 12" aria-hidden="true"><path d="M1 2.5h10v7H1z M1.5 3l4.5 3.5L10.5 3" stroke="#fff" stroke-width="0.9"/></svg>
          <span>info@panelmedic.com</span>
        </li>
        <li>
          <svg viewBox="0 0 12 12" aria-hidden="true"><circle cx="6" cy="6" r="5"/><path d="M1 6h10M6 1c-2 2.5-2 7.5 0 10M6 1c2 2.5 2 7.5 0 10" stroke="#fff" stroke-width="0.8" fill="none"/></svg>
          <span>www.panelmedic.com</span>
        </li>
      </ul>
    </div>
  </section>

  <section class="card card-back">
    <p class="brand-name"><span class="brand-dot"></span>Portal Panel Medic</p>
    <p class="tagline">Expert service at an affordable price</p>
  </section>
</body>
</html>
```